Stationery Design Project

see attached logo and business card layout, envelopes, letterhead, proposal, and invoice stationery needs to all flow.

Industry/Entity Type

Business

```html
<!DOCTYPE html>
<html lang="en">
<head>
<meta charset="utf-8">
<title>Ridgeline Paving Letterhead</title>
<link rel="stylesheet" href="https://fonts.googleapis.com/css2?family=Lato:wght@400;700&family=Arimo:wght@400&display=swap">
<style>
  :root {
    --paper: #ffffff;
    --ink: #1a1a1a;
    --ink-soft: #2b2b2b;
    --gold: #f2c200;
    --tan-light: #f3e2c6;
    --tan: #d8b98a;
    --brown: #8a6a3e;
    --olive: #a89a4a;
    --orange: #f28a1a;
    --orange-light: #ffc34a;
    --red: #d9421a;
    --pattern: #eeeeee;
  }
  * { margin: 0; padding: 0; box-sizing: border-box; }
  html, body { width: 849px; height: 1200px; overflow: hidden; background: var(--paper); }
  .letterhead { position: relative; width: 849px; height: 1200px; background: var(--paper); overflow: hidden; }
  .header-swoosh { position: absolute; left: 0; top: 0; width: 849px; height: 200px; }
  .brand { position: absolute; right: 13px; top: 86px; text-align: right; }
  .brand-name {
    display: flex; align-items: center; justify-content: flex-end; gap: 10px;
    font-family: "Lato", sans-serif; font-weight: 700; font-size: 42px;
    letter-spacing: 0.5px; color: var(--ink); line-height: 1; white-space: nowrap;
  }
  .brand-dot { width: 20px; height: 20px; border-radius: 50%; background: var(--gold); }
  .brand-tagline {
    font-family: "Arimo", sans-serif; font-size: 19px; color: var(--ink-soft);
    margin-top: 6px; line-height: 1; white-space: nowrap;
  }
  .contact {
    position: absolute; font-family: "Lato", sans-serif; font-size: 11.5px;
    color: var(--ink); text-align: right; white-space: nowrap;
  }
  .contact-web { right: 561px; top: 141px; line-height: 13.5px; }
  .contact-post { right: 588px; top: 175px; line-height: 15px; }
  .footer-pattern {
    position: absolute; left: 0; top: 980px; width: 849px; height: 190px;
    background: linear-gradient(180deg, rgba(238,238,238,0) 0%, var(--pattern) 55%, rgba(238,238,238,0.4) 100%);
  }
  .footer-wave { position: absolute; left: 0; bottom: 0; width: 849px; height: 60px; }
</style>
</head>
<body>
<main class="letterhead">
  <svg class="header-swoosh" viewBox="0 0 849 200" aria-hidden="true">
    <defs>
      <linearGradient id="swooshFill" x1="0" y1="0" x2="1" y2="0">
        <stop offset="0" stop-color="var(--brown)"/>
        <stop offset="0.35" stop-color="var(--tan)"/>
        <stop offset="0.8" stop-color="var(--tan-light)"/>
        <stop offset="1" stop-color="#ffffff" stop-opacity="0.6"/>
      </linearGradient>
      <linearGradient id="lineFill" x1="0" y1="0" x2="1" y2="0">
        <stop offset="0" stop-color="var(--olive)"/>
        <stop offset="0.7" stop-color="var(--olive)"/>
        <stop offset="1" stop-color="var(--olive)" stop-opacity="0"/>
      </linearGradient>
    </defs>
    <path d="M0,124 C250,118 480,100 720,62 L849,44 L849,118 C600,126 300,132 0,140 Z" fill="url(#swooshFill)" opacity="0.85"/>
    <path d="M0,136 C300,130 560,124 849,118 L849,121 C560,127 300,134 0,140 Z" fill="var(--brown)" opacity="0.7"/>
    <path d="M0,166 L760,162 L760,164 L0,169 Z" fill="url(#lineFill)"/>
  </svg>

  <div class="brand">
    <div class="brand-name"><span class="brand-dot"></span>RIDGELINE PAVING</div>
    <div class="brand-tagline">Built on Reliable Service</div>
  </div>

  <div class="contact contact-web">
    E: info@ridgeline-paving.com<br>www.ridgeline-paving.com
  </div>
  <div class="contact contact-post">
    4510 harbor dr suite 120 vista, ca 92081<br>p.555.210.4400, f.555.210.4402, c.555.790.3100
  </div>

  <div class="footer-pattern" role="img" aria-label="Faint grey perspective pavement pattern"></div>

  <svg class="footer-wave" viewBox="0 0 849 60" preserveAspectRatio="none" aria-hidden="true">
    <defs>
      <linearGradient id="waveFill" x1="0" y1="0" x2="1" y2="0">
        <stop offset="0" stop-color="var(--orange-light)"/>
        <stop offset="0.6" stop-color="var(--orange)"/>
        <stop offset="1" stop-color="var(--red)"/>
      </linearGradient>
    </defs>
    <path d="M0,14 C300,12 600,20 849,44 L849,60 L0,60 Z" fill="url(#waveFill)"/>
    <path d="M0,40 C300,38 600,44 849,56 L849,60 L0,60 Z" fill="var(--red)" opacity="0.8"/>
  </svg>
</main>
</body>
</html>
```